Mental Health Therapy Website

I need a design for a mental health therapy website. It is a private practice. The business name is Brindle Counseling, PLLC. My name is Martin Hale, LMHC, NCC, DCC. I would like some of the features/menus to be Home; Welcome/About Me, Rates and Services, Common Questions, and Contact.
If possible I would like a blog on the main page that I can update with articles I write. I would like the contact page to feature a map to my location (4318 Cedarbend Ave. E, Lakewood, WA 98499).
I would like to place a small photo of me on the Welcome/About page.
I am new to this so if I am forgetting anything, please ask me!!
I will upload my logo so you can fit it and the color scheme into the design.
Thank you so very much!

```html
<!DOCTYPE html>
<html lang="en">
<head>
<meta charset="utf-8">
<title>Brindle Counseling</title>
<link rel="stylesheet" href="https://fonts.googleapis.com/css2?family=Cinzel:wght@400;700&family=Open+Sans:ital,wght@0,400;0,600;0,700;1,400&display=swap">
<style>
:root{
  --blue:#1f5c9c;
  --blue-dark:#174a80;
  --green:#5d9a2e;
  --green-dark:#4c8424;
  --text:#666;
  --text-dark:#333;
  --header-bg:#eeeeee;
  --page-bg:#fbfcfc;
  --band-bg:#ededed;
  --footer-bg:#262626;
  --rule:#cfcfcf;
}
*{box-sizing:border-box;margin:0;padding:0}
html,body{width:958px;height:1200px;overflow:hidden}
body{position:relative;background:var(--page-bg);font-family:"Open Sans",Arial,sans-serif;color:var(--text)}
.abs{position:absolute}
.site-header{left:0;top:0;width:958px;height:90px;background:var(--header-bg);border-top:3px solid var(--blue-dark)}
.brand{left:127px;top:26px;display:flex;align-items:center;gap:8px}
.brand-mark{width:40px;height:40px;border-radius:50%;background:var(--green)}
.brand-name{font-family:"Cinzel",serif;font-size:22px;color:var(--blue);line-height:1}
.call{left:455px;top:34px;display:flex;align-items:center;gap:6px;font-size:13px;color:#888}
.call strong{color:var(--blue-dark);font-weight:600}
.btn-appt{left:666px;top:25px;width:166px;height:37px;background:linear-gradient(#2f6db0,#1b4f8c);color:#fff;font-family:"Cinzel",serif;font-size:11.5px;font-weight:700;display:flex;align-items:center;justify-content:center;border-radius:2px;box-shadow:0 1px 3px rgba(0,0,0,.3)}
.main-nav{left:0;top:90px;width:958px;height:39px;background:linear-gradient(#6aab35,#528c27);border-top:1px solid #8cc25a}
.main-nav span{position:absolute;top:11px;transform:translateX(-50%);color:#fff;font-family:"Cinzel",serif;font-size:12.5px;white-space:nowrap;letter-spacing:.3px}
.hero{left:0;top:129px;width:958px;height:298px;background:radial-gradient(circle at 53% 6%,#fff3c0 0%,#f2b84a 10%,#a9621c 32%,#4a2a13 62%,#221a16 100%)}
.hero-title{left:587px;top:305px;font-family:"Cinzel",serif;color:#fff;font-size:25px;line-height:30px;text-shadow:0 1px 3px rgba(0,0,0,.5)}
.hero-sub{left:588px;top:376px;color:#fff;font-size:12.5px}
.hero-shadow{left:180px;top:427px;width:600px;height:20px;background:radial-gradient(ellipse at top,rgba(0,0,0,.18),transparent 70%)}
.section-title{font-family:"Cinzel",serif;color:var(--blue);font-size:19px;letter-spacing:.5px;text-align:center}
.about-title{left:0;top:462px;width:958px}
.portrait{left:186px;top:501px;width:108px;height:108px;border-radius:50%;background:radial-gradient(circle at 50% 40%,#e9d6c7,#b9a08f 45%,#2a2a2a 75%)}
.about-text{left:323px;top:505px;width:440px;font-size:12.5px;line-height:18px}
.about-text p+p{margin-top:18px}
.about-text b{color:#444;font-weight:700}
.col{top:650px;width:224px}
.col h2{font-family:"Cinzel",serif;color:var(--blue);font-size:19px;font-weight:400;text-align:center;height:36px}
.col .rule{height:4px;border-top:1px dotted var(--rule);border-bottom:1px dotted var(--rule);margin-bottom:16px}
.col p{font-size:12.5px;line-height:18px;margin-bottom:18px}
.col ul{list-style:none}
.col li{font-size:12.5px;line-height:24px;padding-left:12px;position:relative}
.col li::before{content:"";position:absolute;left:0;top:8px;border-left:4px solid #777;border-top:4px solid transparent;border-bottom:4px solid transparent}
.col li.strong{font-weight:600;color:#555}
.news-item{margin-bottom:14px}
.news-item h3{font-family:"Cinzel",serif;color:var(--green);font-size:10.5px;font-weight:700;text-decoration:underline;margin:0 0 6px 2px}
.news-body{display:flex;gap:12px}
.news-thumb{width:64px;height:54px;flex:none}
.news-body p{font-size:8.5px;line-height:13.5px;margin:0}
.news-body small{display:block;font-size:7.5px;font-weight:700;color:#555;margin-top:4px}
.testi-title{left:0;top:915px;width:958px}
.testi{top:953px;width:345px;height:112px;background:#f5f5f5;border:1px solid #ddd;box-shadow:0 2px 3px rgba(0,0,0,.12)}
.avatar{position:absolute;left:36px;top:23px;width:66px;height:66px;border-radius:50%}
.quote{position:absolute;left:122px;top:27px;width:200px;font-size:9.5px;line-height:15px;font-style:italic}
.cite{position:absolute;left:122px;top:82px;font-size:9.5px;color:#444}
.cite b{color:#222}
.news-band{left:0;top:1098px;width:958px;height:67px;background:var(--band-bg);border-top:1px solid #ddd}
.nl-title{left:121px;top:1116px;font-family:"Cinzel",serif;color:var(--green);font-size:12.5px;font-weight:700}
.nl-sub{left:121px;top:1133px;font-size:9px;color:#888}
.nl-input{left:324px;top:1117px;width:260px;height:29px;background:#fff;border:1px solid #ccc;font-size:9px;color:#888;padding:9px 12px}
.nl-btn{left:583px;top:1117px;width:82px;height:29px;background:linear-gradient(#7ab444,#5d9a2e);color:#fff;font-weight:700;font-size:11px;display:flex;align-items:center;justify-content:center;border:1px solid var(--blue)}
.social{top:1119px;width:26px;height:26px;background:#5a6e86;border-radius:2px}
.site-footer{left:0;top:1165px;width:958px;height:35px;background:var(--footer-bg)}
.copy{left:120px;top:1177px;font-size:9px;color:#999}
.foot-links{left:657px;top:1177px;font-size:9px;color:#999;word-spacing:2px}
</style>
</head>
<body>
<header class="abs site-header"></header>
<div class="abs brand"><span class="brand-mark"></span><span class="brand-name">Brindle<br>Counseling</span></div>
<div class="abs call">
  <svg width="18" height="18" viewBox="0 0 18 18"><rect width="18" height="18" rx="3" fill="#1f5c9c"/><path d="M5 4.5l2 0 1 3-1.3 1a7 7 0 0 0 2.8 2.8l1-1.3 3 1v2c0 .6-.4 1-1 1A9 9 0 0 1 4 5.5c0-.6.4-1 1-1z" fill="#fff"/></svg>
  <span>Call us today <strong>+1800.555.0142</strong></span>
</div>
<div class="abs btn-appt">Schedule Appointment</div>

<nav class="abs main-nav">
  <span style="left:189px">Home</span>
  <span style="left:291px">About Me</span>
  <span style="left:438px">Rates and Services</span>
  <span style="left:617px">Common Questions</span>
  <span style="left:762px">Contact</span>
</nav>

<div class="abs hero" role="img" aria-label="Photo of a person seen from behind against warm evening sunlight"></div>
<div class="abs hero-title">You don’t have to<br>suffer any longer.</div>
<div class="abs hero-sub">Let’s talk and take the next step toward healing.</div>
<div class="abs hero-shadow"></div>

<h1 class="abs section-title about-title" style="font-weight:400">About Me</h1>
<div class="abs portrait" role="img" aria-label="Portrait photo of the therapist"></div>
<div class="abs about-text">
  <p>I am a <b>trauma certified</b> therapist that utilizes CBT+ to assist with trauma.</p>
  <p>My approach to therapy is psychodynamic that utilizes tools from CBT, Solutions-focused, Emotions-focused, and Psychoeducation therapies to assist clients managing depression, anxiety, trauma, phobias, personality disorders, ADHD, self-injury,and communication issues.</p>
</div>

<section class="abs col" style="left:130px">
  <h2>Services</h2><div class="rule"></div>
  <p>Lorem ipsum dolor sit amet, consecte-tur adipisicing elit, sed do eiusmod tempor incididunt ut labore et dolore.</p>
  <ul><li>Counselling</li><li>General Counselling</li><li>Trauma Therapy</li><li>Consultation</li></ul>
</section>
<section class="abs col" style="left:368px">
  <h2>Consultation Hours</h2><div class="rule"></div>
  <p>Lorem ipsum dolor sit amet, consecte-tur adipisicing elit, sed do eiusmod tempor incididunt ut labore et dolore.</p>
  <ul><li class="strong">Monday - Friday</li><li class="strong">9:00 am - 6:00pm</li><li>Call us at: +1800.555.0142</li><li>Email: info@brindlecounselling.com</li></ul>
</section>
<section class="abs col" style="left:607px">
  <h2>Latest News</h2><div class="rule"></div>
  <article class="news-item">
    <h3>Trauma Therapy Can Help</h3>
    <div class="news-body"><div class="news-thumb" role="img" aria-label="Photo of a hooded person sitting alone" style="background:linear-gradient(#d8dbe0,#6f6a68)"></div>
    <div><p>The point of using Lorem Ipsum is that it has a more-or-less normal distribution of letters, as opposed..</p><small>&#9636; 8 December 2013</small></div></div>
  </article>
  <article class="news-item">
    <h3>5 Tips for better outlook in life</h3>
    <div class="news-body"><div class="news-thumb" role="img" aria-label="Photo of a misty lake with a wooden post" style="background:linear-gradient(#cfe0d2,#7f9a7a)"></div>
    <div><p>The point of using Lorem Ipsum is that it has a more-or-less normal distribution of letters, as opposed..</p><small>&#9636; 8 December 2013</small></div></div>
  </article>
</section>

<h2 class="abs section-title testi-title" style="font-weight:400">Client Testimonials</h2>
<div class="abs testi" style="left:124px">
  <div class="avatar" role="img" aria-label="Client portrait photo" style="background:radial-gradient(#c99d80,#5a4436)"></div>
  <p class="quote">“Lorem ipsum dolor sit amet, consectetur adipisicing elit, sed do eiusmod tempor incididunt ut labore et dolore magna aliqua.</p>
  <p class="cite"><b>Daniel Wren</b> &nbsp;| &nbsp;Harbor Co.</p>
</div>
<div class="abs testi" style="left:484px">
  <div class="avatar" role="img" aria-label="Client portrait photo" style="background:radial-gradient(#d9a98c,#3d2a22)"></div>
  <p class="quote">“Lorem ipsum dolor sit amet, consectetur adipisicing elit, sed do eiusmod tempor incididunt ut labore et dolore magna aliqua.</p>
  <p class="cite"><b>Daniel Wren</b> &nbsp;| &nbsp;Harbor Co.</p>
</div>

<div class="abs news-band"></div>
<div class="abs nl-title">Subscribe to our Newsletter</div>
<div class="abs nl-sub">Get the latest updates about mental health</div>
<div class="abs nl-input">Enter Your Email Address</div>
<div class="abs nl-btn">Submit</div>
<div class="abs social" style="left:712px" aria-label="Social link"></div>
<div class="abs social" style="left:746px" aria-label="Social link"></div>
<div class="abs social" style="left:779px" aria-label="Social link"></div>
<div class="abs social" style="left:813px" aria-label="Social link"></div>

<footer class="abs site-footer"></footer>
<div class="abs copy">Copyright © 2014 BrindleCounselling All Rights Reserved.</div>
<div class="abs foot-links">Site Map &nbsp;•&nbsp; Privacy Policy &nbsp;•&nbsp; Contact Us</div>
</body>
</html>
```